Vyrella Motion Design
Would like the design to go over the page in a way that can type over it.
We are a personal training and small group studio
Want it to be professional and classy
Reason: Asked for some modifications on a few designs, want to give the designers time to do this
Target Market(s)
All age groups, sports professionals as well as business professionals, families
Industry/Entity Type
Training
Requirements
Must have
- Must have Vyrella Motion Studio
Mira Pendleby
314 Calloway Street
Marbeck Vale
Northvale Region 7413
Phone: 0497318260
Nice to have
- Professional classy fonts
Colour
Should not have
- Clip art
Balloons

```html
<!DOCTYPE html>
<html lang="en">
<head>
<meta charset="utf-8">
<title>Vyrella Motion Studio Letterhead</title>
<link rel="stylesheet" href="https://fonts.googleapis.com/css2?family=Cabin:wght@400;700&display=swap">
<style>
  :root {
    --paper: #ffffff;
    --ink: #111111;
    --brand-blue: #1d5fa9;
    --swoosh-blue: #27a6e1;
    --swoosh-orange: #ec6a24;
    --ghost: #eef1f5;
  }
  html, body {
    margin: 0;
    padding: 0;
    overflow: hidden;
    background: var(--paper);
  }
  .letterhead {
    position: relative;
    width: 848px;
    height: 1200px;
    overflow: hidden;
    background: var(--paper);
    font-family: "Cabin", "Gill Sans", sans-serif;
  }
  .swooshes {
    position: absolute;
    inset: 0;
    width: 848px;
    height: 1200px;
  }
  .swoosh-blue { fill: var(--swoosh-blue); }
  .swoosh-orange { fill: var(--swoosh-orange); }

  .ghost-name {
    position: absolute;
    margin: 0;
    font-weight: 700;
    line-height: 1;
    color: var(--ghost);
    white-space: nowrap;
    transform: rotate(-90deg);
    transform-origin: left top;
  }
  .ghost-name--main { left: 272px; top: 900px; font-size: 110px; }
  .ghost-name--sub { left: 400px; top: 485px; font-size: 92px; }

  .brand {
    position: absolute;
    left: 24px;
    top: 34px;
    display: flex;
    align-items: center;
    gap: 12px;
  }
  .brand-dot {
    width: 26px;
    height: 26px;
    border-radius: 50%;
    background: var(--swoosh-orange);
  }
  .brand-name {
    margin: 0;
    font-weight: 700;
    font-size: 34px;
    line-height: 1;
    color: var(--brand-blue);
  }

  .contact {
    position: absolute;
    left: 576px;
    top: 112px;
    margin: 0;
    font-style: normal;
    font-size: 23px;
    line-height: 31px;
    color: var(--ink);
    white-space: nowrap;
  }
  .contact .small { font-size: 19px; }
</style>
</head>
<body>
<main class="letterhead">
  <p class="ghost-name ghost-name--main" aria-hidden="true">Vyrella Motion</p>
  <p class="ghost-name ghost-name--sub" aria-hidden="true">Studio</p>

  <svg class="swooshes" viewBox="0 0 848 1200" aria-hidden="true">
    <path class="swoosh-blue" d="M0,205 Q330,105 848,66 L848,76 Q330,135 0,258 Z"/>
    <path class="swoosh-orange" d="M0,192 Q320,92 848,56 L848,68 Q330,112 0,212 Z"/>
    <path class="swoosh-blue" d="M0,1116 Q520,1092 848,948 L848,972 Q530,1108 0,1126 Z"/>
    <path class="swoosh-orange" d="M0,1126 Q530,1110 848,972 L848,990 Q530,1126 0,1136 Z"/>
  </svg>

  <header class="brand">
    <span class="brand-dot" aria-hidden="true"></span>
    <p class="brand-name">Vyrella Motion Studio</p>
  </header>

  <address class="contact">
    Vyrella Motion Studio<br>
    Mira Pendleby<br>
    <span class="small">314</span> Calloway Street<br>
    Marbeck Vale<br>
    Northvale Region <span class="small">7413</span><br>
    Phone number <span class="small">0497318260</span>
  </address>
</main>
</body>
</html>
```